Kestrel Photography Business Card

I need a business card designed for a photography business based in Perth, Western Australia called Kestrel Photography.

We specialise in wedding, event photography and portrait photography.

The business card must borrow the style of the attached logo.

The hex codes for the colours in the logo are:
#ED1D85 - Pink
#89C23E - Green
#37282F - Black

The name on the card will be:
Name: Toviran
Phone: 0417395268
Website: www.kestrelphotography.com.au
Facebook: kestrelphotography

I am open and happy to accept creative concepts.

I’d like some space at the back for writing notes and appointment details.

```html
<!DOCTYPE html>
<html lang="en">
<head>
<meta charset="utf-8">
<title>Kestrel Photography – Business Card</title>
<link href="https://fonts.googleapis.com/css2?family=Open+Sans:ital,wght@0,300;1,300&family=Raleway:wght@400&display=swap" rel="stylesheet">
<style>
  :root {
    --pink: #ED1D85;
    --green: #89C23E;
    --ink: #37282F;
    --text-grey: #4a4446;
    --card-light: #f4f3f1;
    --card-edge: #bdb9b3;
    --note-tint: #e4e1dc;
    --page: #e9e6e1;
    --scene-glow: #d9b57a;
    --scene-mid: #8a6a3e;
    --scene-dark: #2e2418;
  }
  html, body {
    margin: 0;
    padding: 0;
    width: 1200px;
    height: 900px;
    overflow: hidden;
    background: var(--page);
  }
  .canvas {
    position: relative;
    width: 1200px;
    height: 900px;
  }
  .card {
    position: absolute;
    top: 300px;
    width: 510px;
    height: 300px;
    overflow: hidden;
    background: radial-gradient(ellipse at 50% 35%, var(--card-light) 40%, var(--card-edge) 100%);
    box-shadow: 0 6px 18px rgba(0,0,0,0.18);
  }
  .card--front { left: 60px; }
  .card--back { left: 630px; }

  /* Front */
  .brand-mark {
    position: absolute;
    left: 50%;
    top: 22px;
    width: 96px;
    height: 96px;
    margin-left: -48px;
    border-radius: 50%;
    background: var(--pink);
  }
  .wordmark {
    position: absolute;
    left: 0;
    right: 0;
    top: 146px;
    margin: 0;
    padding-left: 0.58em;
    text-align: center;
    font-family: "Raleway", sans-serif;
    font-weight: 400;
    font-size: 19px;
    letter-spacing: 0.58em;
    text-transform: uppercase;
    color: var(--ink);
  }
  .landscape {
    position: absolute;
    left: 0;
    right: 0;
    bottom: 0;
    height: 125px;
    background:
      linear-gradient(to bottom, rgba(244,243,241,0) 0%, rgba(217,181,122,0.55) 25%, var(--scene-mid) 55%, var(--scene-dark) 100%);
  }

  /* Back */
  .contact {
    position: absolute;
    left: 52px;
    top: 26px;
    font-family: "Open Sans", sans-serif;
    font-weight: 300;
    color: var(--text-grey);
  }
  .contact__name {
    margin: 0 0 4px;
    font-size: 26px;
    font-weight: 300;
    letter-spacing: 0.06em;
    color: var(--ink);
  }
  .contact__line {
    margin: 0;
    font-size: 17px;
    font-style: italic;
    line-height: 23px;
    letter-spacing: 0.04em;
  }
  .contact__social {
    display: flex;
    align-items: center;
    gap: 6px;
  }
  .contact__social-box {
    width: 12px;
    height: 12px;
    border: 1.5px solid var(--text-grey);
    border-radius: 2px;
  }
  .notes-area {
    position: absolute;
    right: 0;
    bottom: 0;
    width: 190px;
    height: 130px;
    background: radial-gradient(ellipse at 70% 70%, var(--note-tint) 0%, rgba(228,225,220,0) 75%);
  }
</style>
</head>
<body>
<main class="canvas">
  <section class="card card--front" aria-label="Card front">
    <div class="brand-mark" aria-hidden="true"></div>
    <h1 class="wordmark">Kestrel Photography</h1>
    <div class="landscape" role="img" aria-label="Sepia photograph of a kestrel against a sunlit grass field at dusk"></div>
  </section>

  <section class="card card--back" aria-label="Card back">
    <div class="contact">
      <h2 class="contact__name">Toviran</h2>
      <p class="contact__line">0417395268</p>
      <p class="contact__line">www.kestrelphotography.com.au</p>
      <p class="contact__line contact__social"><span class="contact__social-box" aria-hidden="true"></span>kestrelphotography</p>
    </div>
    <div class="notes-area" role="img" aria-label="Decorative camera viewfinder guide lines framing space for notes"></div>
  </section>
</main>
</body>
</html>
```